Trade Show Booth Artwork

We are a software company that delivers education-specific applications to help both small and large education institutions better manage their facilities, IT and business operations. We are looking for artwork for a new trade show booth. This new booth will be a table top display that contains four different areas, or squares of fabric, for graphics and text. In the attached document you will find a picture of a sample booth and also the dimensions for each square.

We are looking for artwork for a total of 5 squares, even though the booth only accommodates 4 squares at a time. Also, attached in the brief is a description of what needs to be placed on each square in terms of a graphic or text. We would like two of the squares to be visual or graphic and the other two to be text or copy. We have provided the style guide for our website which includes all of our current colors and fonts. You may also visit our website www.campusforge.com to get a better idea of our brand.

Feel free to add background elements to the squares that contain copy to make it more visually appealing. The school building graphic that is attached can be used as the graphic for one of the panels, but we are open to similar ideas or graphics instead of the school building provided.

We will need the original Adobe Illustrator file with fonts and links from the design that is chosen.

Industry/Entity Type

Education

```html
<!DOCTYPE html>
<html lang="en">
<head>
<meta charset="UTF-8">
<title>Booth Panel – Mission Copy</title>
<link href="https://fonts.googleapis.com/css2?family=Carlito&display=swap" rel="stylesheet">
<style>
  :root {
    --canvas-bg: #ffffff;
    --canvas-border: #000000;
    --panel-teal: #77d1d4;
    --panel-glow: rgba(255, 255, 255, 0.22);
    --copy-color: #eef9f9;
  }
  * { margin: 0; padding: 0; box-sizing: border-box; }
  html, body {
    width: 1200px;
    height: 1001px;
    overflow: hidden;
    background: var(--canvas-bg);
  }
  .canvas {
    position: relative;
    width: 1200px;
    height: 1001px;
    border: 2px solid var(--canvas-border);
    background: var(--canvas-bg);
  }
  .booth-panel {
    position: absolute;
    left: 224px;
    top: 99px;
    width: 755px;
    height: 808px;
    background: var(--panel-teal);
    overflow: hidden;
  }
  .panel-backdrop {
    position: absolute;
    left: 0;
    top: 0;
    width: 755px;
    height: 808px;
  }
  .panel-copy {
    position: absolute;
    left: 116px;
    top: 121px;
    width: 560px;
    font-family: "Carlito", "Calibri", sans-serif;
    font-size: 34px;
    line-height: 46px;
    color: var(--copy-color);
    list-style: none;
  }
  .panel-copy li + li { margin-top: 47px; }
</style>
</head>
<body>
  <div class="canvas">
    <section class="booth-panel">
      <svg class="panel-backdrop" viewBox="0 0 755 808" role="img" aria-label="Faint outlined lightbulb illustration inside a large circle, used as a background decoration">
        <defs>
          <radialGradient id="backdropGlow" cx="50%" cy="50%" r="50%">
            <stop offset="0%" stop-color="#ffffff" stop-opacity="0.10"/>
            <stop offset="85%" stop-color="#ffffff" stop-opacity="0.06"/>
            <stop offset="100%" stop-color="#ffffff" stop-opacity="0.14"/>
          </radialGradient>
        </defs>
        <circle cx="377" cy="403" r="305" fill="url(#backdropGlow)"/>
      </svg>
      <ul class="panel-copy">
        <li>• Serving as the market leader in<br>cloud asset management</li>
        <li>• Delivering education-specific<br>applications to help both small<br>and large institutions better<br>manage their facilities, IT and<br>business operations</li>
      </ul>
    </section>
  </div>
</body>
</html>
```